Business Card Design

We need a business card for a new business based in Sydney, Australia. It is a home based baking business, the key products are cookies and muffins and slices including gluten free baked goods. With the emphasis on home made baking. The target market is cafes, coffee shops and vans, restaurants. Products may be provided in display jars or individually wrapped. The final design should be in the colours pink, purple.

Industry/Entity Type

Business

Contact Information for Business Card

Pindle's Bakery Pty Ltd, Maren Tulloch, maren@pindlesbakery.com.au
0412 506 218, www.pindlesbakery.com.au, ACN 581 246 037,

```html
<!DOCTYPE html>
<html lang="en">
<head>
<meta charset="utf-8">
<title>Pindle's Bakery – Business Card</title>
<link href="https://fonts.googleapis.com/css2?family=Lato:wght@400;700&display=swap" rel="stylesheet">
<style>
  :root {
    --backdrop: #2a2a2a;
    --card: #ffffff;
    --pink: #e4157f;
    --purple: #8a3d9c;
    --muffin-light: #e9b353;
    --muffin-dark: #b9772c;
    --cookie-light: #c79a68;
    --cookie-dark: #8a6240;
    --case-pink: #b0507a;
    --case-tan: #d3a06a;
    --plate-green: #6f9c43;
    --plate-cookie: #d9ad74;
  }
  * { margin: 0; padding: 0; box-sizing: border-box; }
  html, body {
    width: 1200px;
    height: 1000px;
    overflow: hidden;
    background: var(--backdrop);
    font-family: "Lato", Arial, sans-serif;
  }
  .business-card {
    position: absolute;
    left: 100px;
    top: 214px;
    width: 1000px;
    height: 572px;
    background: var(--card);
    overflow: hidden;
  }
  .brand-name {
    position: absolute;
    left: 0;
    right: 0;
    top: 26px;
    text-align: center;
    color: var(--pink);
    font-weight: 400;
    font-size: 62px;
    line-height: 1;
    letter-spacing: 1px;
  }
  .brand-suffix {
    position: absolute;
    right: 262px;
    top: 98px;
    color: var(--purple);
    font-weight: 400;
    font-size: 17px;
    letter-spacing: 1px;
  }
  .photo-strip {
    position: absolute;
    left: 0;
    top: 138px;
    width: 1000px;
    height: 180px;
    display: flex;
  }
  .photo { flex: 1 1 0; height: 100%; }
  .photo-muffins {
    background: radial-gradient(circle at 45% 40%, var(--muffin-light), var(--muffin-dark));
  }
  .photo-cookies-tray {
    background: radial-gradient(circle at 50% 50%, var(--cookie-light), var(--cookie-dark));
  }
  .photo-muffin-cases {
    background: linear-gradient(160deg, var(--case-tan), var(--case-pink));
  }
  .photo-cookie-plate {
    background: radial-gradient(circle at 50% 45%, var(--plate-cookie) 0 40%, var(--plate-green) 72%);
  }
  .tagline {
    position: absolute;
    left: 130px;
    top: 334px;
    color: var(--pink);
    font-size: 20px;
    font-weight: 400;
    letter-spacing: 1px;
    white-space: nowrap;
  }
  .contact-list {
    position: absolute;
    right: 40px;
    top: 372px;
    list-style: none;
    text-align: right;
    font-size: 20px;
    line-height: 28px;
    color: var(--purple);
    white-space: nowrap;
  }
  .contact-label {
    color: var(--pink);
    font-weight: 700;
  }
  .contact-list .phone { color: var(--pink); }
  .person {
    position: absolute;
    left: 130px;
    top: 452px;
  }
  .person-name {
    color: var(--purple);
    font-size: 32px;
    font-weight: 400;
    line-height: 1.1;
  }
  .person-acn {
    color: var(--pink);
    font-size: 21px;
    margin-top: 4px;
  }
</style>
</head>
<body>
  <section class="business-card">
    <h1 class="brand-name">Pindle's Bakery</h1>
    <div class="brand-suffix">PTY. LTD.</div>

    <div class="photo-strip">
      <div class="photo photo-muffins" role="img" aria-label="Photo of golden sugar-topped muffins"></div>
      <div class="photo photo-cookies-tray" role="img" aria-label="Photo of chocolate chip cookies on baking paper"></div>
      <div class="photo photo-muffin-cases" role="img" aria-label="Photo of muffins in pink patterned cases"></div>
      <div class="photo photo-cookie-plate" role="img" aria-label="Photo of chocolate chip cookies on a white plate"></div>
    </div>

    <p class="tagline">Home Made and Gluten Free Cookies, Muffins &amp; Slices.</p>

    <ul class="contact-list">
      <li class="phone"><span class="contact-label">P:</span> 0412 506 218</li>
      <li><span class="contact-label">E:</span> maren@pindlesbakery.com.au</li>
      <li><span class="contact-label">W:</span> www.pindlesbakery.com.au</li>
    </ul>

    <div class="person">
      <div class="person-name">Maren Tulloch</div>
      <div class="person-acn">ACN: 581 246 037</div>
    </div>
  </section>
</body>
</html>
```